KQW Authorised Dealer needs Business Cards

We need a business card designed for our branch owners. Vellmor Alarms is an Authorised KQW Dealer and does its own independent installations outside of the KQW work we perform so whilst the KQW Authorised Dealer Logo needs to be included, it should not be overwhelming in respect of the overall look of the card. I would like a rounded edge to the cards corners rather than a 90 degree hard edge. We also need to promote the fact that we do First Class Alarm & CCTV Solutions. (Details of card holder to follow)

```html
<!DOCTYPE html>
<html lang="en">
<head>
<meta charset="utf-8">
<title>Vellmor Alarms – Business Card</title>
<link href="https://fonts.googleapis.com/css2?family=Oswald:wght@500;600&family=Open+Sans:wght@400;600&display=swap" rel="stylesheet">
<style>
  :root {
    --page: #efefef;
    --white: #ffffff;
    --blue: #1f7bc1;
    --charcoal: #58595b;
    --dark-grey: #5f6062;
    --light-grey: #c9cacc;
    --text-grey: #6d6e70;
  }
  * { box-sizing: border-box; margin: 0; padding: 0; }
  html, body { width: 1057px; height: 1200px; overflow: hidden; }
  body {
    background: var(--page);
    font-family: "Open Sans", Arial, sans-serif;
    position: relative;
  }
  .card {
    position: absolute;
    left: 178px;
    width: 700px;
    height: 400px;
    background: var(--white);
    border-radius: 14px;
    overflow: hidden;
    box-shadow: 0 6px 18px rgba(0,0,0,0.12);
  }
  .card--front { top: 120px; border: 14px solid var(--charcoal); }
  .card--back { top: 660px; }

  .front-frame {
    position: absolute;
    inset: 0;
    border: 8px solid var(--blue);
    display: flex;
    flex-direction: column;
    align-items: center;
    justify-content: center;
    gap: 14px;
  }
  .brand {
    display: flex;
    align-items: center;
    gap: 14px;
  }
  .brand__mark {
    width: 36px;
    height: 36px;
    background: var(--blue);
  }
  .brand__name {
    font-family: "Oswald", "Arial Narrow", sans-serif;
    font-weight: 600;
    font-size: 44px;
    letter-spacing: 1px;
    color: var(--blue);
    line-height: 1;
  }
  .tagline {
    font-size: 13px;
    font-weight: 600;
    letter-spacing: 3px;
    color: var(--text-grey);
    text-transform: uppercase;
  }
  .card--back .brand {
    position: absolute;
    left: 40px;
    top: 30px;
  }
  .card--back .brand__name { font-size: 38px; }
  .card--back .tagline {
    position: absolute;
    left: 90px;
    top: 72px;
    font-size: 10px;
    letter-spacing: 2px;
  }

  .dealer {
    position: absolute;
    right: 30px;
    bottom: 28px;
    display: flex;
    align-items: center;
    gap: 8px;
  }
  .dealer__mark {
    width: 12px;
    height: 12px;
    border-radius: 50%;
    background: var(--dark-grey);
  }
  .dealer__name {
    font-size: 11px;
    font-weight: 600;
    letter-spacing: 1.5px;
    color: var(--dark-grey);
  }

  .bands { position: absolute; inset: 0; }

  .holder {
    position: absolute;
    left: 40px;
    top: 212px;
    color: var(--white);
  }
  .holder__name {
    font-family: "Oswald", "Arial Narrow", sans-serif;
    font-weight: 500;
    font-size: 28px;
    letter-spacing: 2px;
    line-height: 1.1;
  }
  .holder__title {
    font-size: 14px;
    letter-spacing: 3px;
    margin-top: 4px;
  }

  .phones {
    position: absolute;
    left: 400px;
    top: 124px;
    list-style: none;
  }
  .phones li {
    display: flex;
    align-items: center;
    gap: 10px;
    font-size: 16px;
    color: var(--dark-grey);
    letter-spacing: 1px;
    height: 30px;
  }

  .contacts {
    position: absolute;
    left: 40px;
    top: 312px;
    list-style: none;
  }
  .contacts li {
    display: flex;
    align-items: center;
    gap: 10px;
    font-size: 13px;
    color: var(--text-grey);
    height: 26px;
  }
  .icon {
    width: 20px;
    height: 20px;
    flex: none;
  }
</style>
</head>
<body>

  <section class="card card--front" aria-label="Business card front">
    <div class="front-frame">
      <div class="brand">
        <span class="brand__mark"></span>
        <span class="brand__name">VELLMOR ALARMS</span>
      </div>
      <p class="tagline">First Class Alarm &amp; CCTV Solutions</p>
    </div>
  </section>

  <section class="card card--back" aria-label="Business card back">
    <svg class="bands" width="700" height="400" viewBox="0 0 700 400" aria-hidden="true">
      <polygon points="380,92 700,92 700,110 362,110" fill="var(--blue)"/>
      <polygon points="362,110 700,110 700,190 290,190" fill="var(--light-grey)"/>
      <polygon points="0,200 360,200 290,280 0,280" fill="var(--dark-grey)"/>
      <polygon points="0,280 290,280 272,298 0,298" fill="var(--blue)"/>
    </svg>

    <div class="brand">
      <span class="brand__mark"></span>
      <span class="brand__name">VELLMOR ALARMS</span>
    </div>
    <p class="tagline">First Class Alarm &amp; CCTV Solutions</p>

    <ul class="phones">
      <li>
        <svg class="icon" viewBox="0 0 20 20" aria-hidden="true">
          <rect width="20" height="20" fill="var(--blue)"/>
          <path d="M6 4.5l2 .3 1 3-1.3 1a7 7 0 0 0 3.8 3.8l1-1.3 3 1 .3 2c-.2.8-1 1.2-1.8 1.2A10 10 0 0 1 4.8 6.3c0-.8.4-1.6 1.2-1.8z" fill="var(--white)"/>
        </svg>
        014 552 0193
      </li>
      <li>
        <svg class="icon" viewBox="0 0 20 20" aria-hidden="true">
          <rect width="20" height="20" fill="var(--blue)"/>
          <rect x="6" y="3.5" width="8" height="13" rx="1.5" fill="none" stroke="var(--white)" stroke-width="1.6"/>
          <circle cx="10" cy="14" r="0.9" fill="var(--white)"/>
        </svg>
        014 552 0194
      </li>
    </ul>

    <div class="holder">
      <div class="holder__name">DARA QUINLAN</div>
      <div class="holder__title">FOUNDER</div>
    </div>

    <ul class="contacts">
      <li>
        <svg class="icon" viewBox="0 0 20 20" aria-hidden="true">
          <rect width="20" height="20" fill="var(--dark-grey)"/>
          <path d="M10 3.5a4.2 4.2 0 0 0-4.2 4.2c0 3.2 4.2 8.3 4.2 8.3s4.2-5.1 4.2-8.3A4.2 4.2 0 0 0 10 3.5z" fill="var(--white)"/>
          <circle cx="10" cy="7.7" r="1.5" fill="var(--dark-grey)"/>
        </svg>
        21 Harrow Quay, Bellfield Road
      </li>
      <li>
        <svg class="icon" viewBox="0 0 20 20" aria-hidden="true">
          <rect width="20" height="20" fill="var(--dark-grey)"/>
          <rect x="4" y="6" width="12" height="8.5" fill="none" stroke="var(--white)" stroke-width="1.4"/>
          <path d="M4 6l6 5 6-5" fill="none" stroke="var(--white)" stroke-width="1.4"/>
        </svg>
        hello@vellmoralarms.com
      </li>
      <li>
        <svg class="icon" viewBox="0 0 20 20" aria-hidden="true">
          <rect width="20" height="20" fill="var(--dark-grey)"/>
          <circle cx="10" cy="10" r="5.5" fill="none" stroke="var(--white)" stroke-width="1.3"/>
          <path d="M4.5 10h11M10 4.5c-2.4 3-2.4 8 0 11M10 4.5c2.4 3 2.4 8 0 11" fill="none" stroke="var(--white)" stroke-width="1.1"/>
        </svg>
        www.vellmoralarms.com
      </li>
    </ul>

    <div class="dealer">
      <span class="dealer__mark"></span>
      <span class="dealer__name">KQW AUTHORISED DEALER</span>
    </div>
  </section>

</body>
</html>
```